CONTACT US Page and design for website

We need a contact us page for our website. We would like it to have a message area, a map, our information, etc.

Please see the text attachment for what we are looking for. We need to have something that is creative and interesting, modern and professional.

We believe that a contact US page should be very creative because everyone clicks that to contact us. We want it to be super professional, attention grabbing, pleasing to the eye.

PLEASE KEEP THE HEADER AND FOOTER THE SAME, ONLY THE ACTUAL CONTACT US PAGE NEEDS TO BE WORKED ON. THANKS!
We are excited to work with designers for this project.

Target Market(s)

Clients in technology business

Industry/Entity Type

Information Technology

Number of Pages Required

1 page

Font styles to use
Serif

Requirements
Must have
• CHECK THE TEXT ATTACHMENT PLEASE
• Must stay within our design colors and theme.
Nice to have
• see attachment
Should not have
• it should be special

```html
<!DOCTYPE html>
<html lang="en">
<head>
<meta charset="utf-8">
<title>Contact Us – Novalink Tech</title>
<link href="https://fonts.googleapis.com/css2?family=Lato:wght@400;700&family=Montserrat:wght@400;600;700&display=swap" rel="stylesheet">
<style>
:root{
  --dark:#0c4c3f;
  --teal:#2b8c78;
  --aqua:#3ecbbf;
  --brand:#2fb5a6;
  --ink:#222;
  --muted:#555;
  --line:#cfd6d4;
  --foot:#a9a9a9;
  --foot-dark:#9a9a9a;
  --white:#fff;
}
*{box-sizing:border-box;margin:0;padding:0}
html,body{width:806px;height:1200px;overflow:hidden;background:var(--white)}
body{position:relative;font-family:"Lato",sans-serif;color:var(--ink)}
.abs{position:absolute}

/* header */
.brand{left:14px;top:14px;display:flex;align-items:center;gap:8px}
.brand-dot{width:26px;height:26px;border-radius:50%;background:var(--brand)}
.brand-name{font-family:"Montserrat",sans-serif;font-weight:600;font-size:21px;letter-spacing:1px;color:var(--brand)}
.account{left:688px;top:0;width:100px;height:16px;display:flex;font-size:5.5px;color:#666;border-radius:0 0 0 10px;overflow:hidden}
.account span{flex:1;display:flex;align-items:center;justify-content:center;background:#d7d7d7}
.account span+span{background:#c4c4c4}
.quick{left:628px;top:23px;display:flex;align-items:center;gap:8px;font-size:7px;color:#555}
.ring{width:20px;height:20px;border-radius:50%;border:1px solid #ccc;display:flex;align-items:center;justify-content:center}
.quick .phone-num{font-size:10px;color:#333}
.rule{left:0;top:51px;width:806px;height:1px;background:#e5e5e5}
.nav{left:17px;top:59px;display:flex;gap:13px;font-size:7px;color:#555;text-transform:uppercase}
.search{left:632px;top:57px;width:115px;height:15px;border:1px solid #bbb;border-radius:8px;font-size:5.5px;color:#777;padding:4px 14px}
.search svg{position:absolute;right:5px;top:3px}
.cart{left:758px;top:56px;width:18px;height:18px;border-radius:50%;border:1px solid #bbb;display:flex;align-items:center;justify-content:center}
.crumb{left:0;top:77px;width:806px;height:18px;background:var(--aqua);font-size:6px;color:var(--white);font-weight:700;padding:5px 58px;border-top:2px solid #2fa89c}

/* main */
.page-title{left:0;top:108px;width:806px;text-align:center;font-family:"Montserrat",sans-serif;font-weight:700;font-size:23px;color:#111}
.photo{left:14px;top:143px;width:372px;height:365px;background:linear-gradient(180deg,#24313f 0%,#3b3a38 55%,#6b5a3c 80%,#3f4a36 100%)}
.map{left:410px;top:144px;width:376px;height:363px;border:2px solid var(--teal);background:#e6e4df}

.card{top:528px;height:93px;background:var(--teal);color:var(--white)}
.card h2{background:var(--dark);height:30px;font-size:13.5px;font-weight:700;padding:7px 27px}
.card p{display:flex;align-items:center;gap:7px;font-size:12px;padding:0 27px;margin-top:10px}
.card p+p{margin-top:9px}

.panel{left:14px;width:772px;border:2px solid var(--teal);border-top:0}
.panel h2{background:var(--dark);color:var(--white);height:30px;font-size:13.5px;font-weight:700;padding:7px 25px;margin:0 -2px}
.form{top:641px;height:178px}
.field{position:absolute;border:1px solid #7a8f8a;font-size:9.5px;color:#666;padding:9px 7px}
.submit{position:absolute;left:675px;top:93px;width:71px;height:65px;border-radius:4px;background:linear-gradient(135deg,#1c6b58 0%,#0c4c3f 50%,#083d32 100%);color:var(--white);font-size:12px;display:flex;align-items:center;justify-content:center}
.hours{top:839px;height:106px}
.hours-grid{position:absolute;left:24px;top:44px;display:flex;font-size:12px;line-height:24px}
.hours-grid div{padding:0 13px 0 0;margin-right:13px;border-right:2px solid var(--teal)}
.hours-grid div:last-child{padding-right:32px}
.social{position:absolute;left:568px;top:36px}
.social h3{font-weight:400;font-size:16.5px;line-height:20px;margin-bottom:7px}
.social ul{display:flex;gap:5px;list-style:none}
.social li{width:21px;height:21px;background:var(--dark)}

/* footer */
.foot{left:0;top:965px;width:806px;height:145px;background:var(--foot);color:var(--white);text-align:center}
.foot-about{width:390px;margin:11px auto 0;font-size:7.2px;line-height:10px}
.foot-contact{display:flex;justify-content:center;gap:40px;font-size:7px;margin-top:12px;text-align:left}
.foot-contact span{display:flex;gap:5px;align-items:flex-start}
.foot-links{display:flex;justify-content:center;gap:38px;font-size:8px;margin-top:21px}
.foot-links small{display:block;font-size:5px;line-height:7px;margin-top:3px}
.foot-base{left:0;top:1110px;width:806px;height:90px;background:var(--foot-dark)}
.foot-rings{position:absolute;left:343px;top:10px;display:flex;gap:8px}
.foot-rings i{width:20px;height:20px;border-radius:50%;border:1px solid #e0e0e0}
.foot-line{position:absolute;left:40px;top:40px;width:726px;height:1px;background:#b5b5b5}
.foot-mark{position:absolute;left:362px;top:48px;display:flex;gap:5px;font-size:6.5px;color:var(--white);line-height:9px}
.foot-mark b{width:11px;height:11px;border-radius:50%;background:#e5e5e5;margin-top:1px}
</style>
</head>
<body>

<header>
  <div class="abs brand"><span class="brand-dot"></span><span class="brand-name">NOVALINK</span></div>
  <div class="abs account"><span>SIGN UP</span><span>LOGIN</span></div>
  <div class="abs quick">
    <span class="ring"><svg width="10" height="8" viewBox="0 0 10 8"><path d="M1 1h8v4H4L2 7V5H1z" fill="#666"/></svg></span>
    <span>LIVE CHAT</span>
    <span class="ring"><svg width="10" height="10" viewBox="0 0 10 10"><path d="M2 1l2 2-1 1.5c.7 1.3 1.6 2.2 2.8 2.8L7 6l2 2-1.3 1.3C4.5 8.8 1.2 5.5.7 2.3z" fill="var(--teal)"/></svg></span>
    <span class="phone-num">555-014-2290</span>
  </div>
  <div class="abs rule"></div>
  <nav class="abs nav"><span>Servers</span><span>Workstations</span><span>Components</span><span>Virtual Reality</span><span>Drones</span><span>About Us</span><span>Blog</span><span>Resources</span><span>Contact Us</span></nav>
  <div class="abs search">Search<svg width="8" height="8" viewBox="0 0 8 8"><circle cx="3.3" cy="3.3" r="2.3" fill="none" stroke="var(--teal)" stroke-width="1.2"/><path d="M5 5l2.4 2.4" stroke="var(--teal)" stroke-width="1.2"/></svg></div>
  <div class="abs cart"><svg width="10" height="9" viewBox="0 0 10 9"><path d="M1 1h8l-1 5H2z" fill="var(--aqua)"/></svg></div>
  <div class="abs crumb">HOME / CONTACT US</div>
</header>

<main>
  <h1 class="abs page-title">CONTACT US</h1>
  <div class="abs photo" role="img" aria-label="City office towers at dusk with lit windows and a parking lot"></div>
  <div class="abs map" role="img" aria-label="Street map showing the office location on Marlow Ave"></div>

  <section class="abs card" style="left:14px;width:251px">
    <h2>For General Inquiries</h2>
    <p><svg width="11" height="11" viewBox="0 0 10 10"><path d="M2 1l2 2-1 1.5c.7 1.3 1.6 2.2 2.8 2.8L7 6l2 2-1.3 1.3C4.5 8.8 1.2 5.5.7 2.3z" fill="#fff"/></svg>(555)014-2290</p>
    <p><svg width="11" height="8" viewBox="0 0 11 8"><rect x=".5" y=".5" width="10" height="7" fill="none" stroke="#fff"/><path d="M.5.5l5 4 5-4" fill="none" stroke="#fff"/></svg>info@novalinktech.com</p>
  </section>
  <section class="abs card" style="left:285px;width:231px">
    <h2>For Purchasing Inquiries</h2>
    <p><svg width="11" height="11" viewBox="0 0 10 10"><path d="M2 1l2 2-1 1.5c.7 1.3 1.6 2.2 2.8 2.8L7 6l2 2-1.3 1.3C4.5 8.8 1.2 5.5.7 2.3z" fill="#fff"/></svg>(555)014-2290</p>
    <p><svg width="11" height="8" viewBox="0 0 11 8"><rect x=".5" y=".5" width="10" height="7" fill="none" stroke="#fff"/><path d="M.5.5l5 4 5-4" fill="none" stroke="#fff"/></svg>purchasing@novalinktech.com</p>
  </section>
  <section class="abs card" style="left:535px;width:251px">
    <h2>Sales Inquiries</h2>
    <p><svg width="11" height="11" viewBox="0 0 10 10"><path d="M2 1l2 2-1 1.5c.7 1.3 1.6 2.2 2.8 2.8L7 6l2 2-1.3 1.3C4.5 8.8 1.2 5.5.7 2.3z" fill="#fff"/></svg>(555)014-2290</p>
    <p><svg width="11" height="8" viewBox="0 0 11 8"><rect x=".5" y=".5" width="10" height="7" fill="none" stroke="#fff"/><path d="M.5.5l5 4 5-4" fill="none" stroke="#fff"/></svg>sales@novalinktech.com</p>
  </section>

  <section class="abs panel form">
    <h2>Contact Form</h2>
    <div class="field" style="left:24px;top:49px;width:223px;height:30px">Your Full Name:</div>
    <div class="field" style="left:273px;top:49px;width:223px;height:30px">Your Email Address:</div>
    <div class="field" style="left:521px;top:49px;width:223px;height:30px">Phone Number :</div>
    <div class="field" style="left:24px;top:93px;width:622px;height:64px">Message:</div>
    <div class="submit">SUBMIT</div>
  </section>

  <section class="abs panel hours">
    <h2>Hours of Operation</h2>
    <div class="hours-grid">
      <div>Monday:&nbsp;&nbsp; 8:00am- 5:00pm<br>Thursday: 8:00am- 5:00pm</div>
      <div>Tuesday: 8:00am- 5:00pm<br>Friday:&nbsp;&nbsp;&nbsp; 8:00am- 5:00pm</div>
      <div>Wednesday: 8:00am- 5:00pm<br>Saturday &amp; Sunday closed</div>
    </div>
    <div class="social">
      <h3>Social Media</h3>
      <ul><li></li><li></li><li></li><li></li><li></li><li></li></ul>
    </div>
  </section>
</main>

<footer>
  <div class="abs foot">
    <p class="foot-about">Based in Westfield Park, California, Novalink Tech builds custom servers, storage and workstations for local firms across the valley, the coast and the southern counties. Novalink Tech also delivers these products to clients throughout the United States and worldwide.</p>
    <div class="foot-contact">
      <span><svg width="6" height="8" viewBox="0 0 6 8"><path d="M3 0a3 3 0 0 1 3 3c0 2-3 5-3 5S0 5 0 3a3 3 0 0 1 3-3z" fill="#fff"/></svg>4120 Marlow Ave.<br>Westfield Park, CA 91000</span>
      <span><svg width="7" height="7" viewBox="0 0 10 10"><path d="M2 1l2 2-1 1.5c.7 1.3 1.6 2.2 2.8 2.8L7 6l2 2-1.3 1.3C4.5 8.8 1.2 5.5.7 2.3z" fill="#fff"/></svg>555-014-2290</span>
      <span><svg width="8" height="6" viewBox="0 0 11 8"><rect width="11" height="8" fill="#fff"/></svg>sales@novalinktech.com</span>
    </div>
    <div class="foot-links">
      <span>Computer Hardware</span><span>Drones</span><span>Virtual Reality</span><span>About Us</span>
      <span>Customer Support<small>Terms and Conditions<br>Warranty Information<br>Contact Us<br>Return Policy</small></span>
    </div>
  </div>
  <div class="abs foot-base">
    <div class="foot-rings"><i></i><i></i><i></i><i></i></div>
    <div class="foot-line"></div>
    <div class="foot-mark"><b></b><span>Novalink Tech, LLC.<br>Copyright © 2017</span></div>
  </div>
</footer>

</body>
</html>
```